Stationery Design Project for Holloway Kenbukan Karate Studio

We Need a Stationery Design for a Karate School Teaching Okinawa Shorin Ryu Karate in Marlowe, Florida, U.S.A.

Target Market(s)

Adults Base Western Speaking aged between 25 and 65 yrs, old that handle household budgets

Industry/Entity Type

School

Requirements
Must have
• Name of business: Holloway Kenbukan Karate Studio
Address: Larkspur Commons 18342 US Hwy. 91
Marlowe, Florida. 33914
Phone # : 407-555-0183
email : Hollowaykenbukanstudio@mailgrove.example
Logo - attatched

```html
<!DOCTYPE html>
<html lang="en">
<head>
<meta charset="utf-8">
<title>Holloway Kenbukan Karate Studio – Business Cards</title>
<link href="https://fonts.googleapis.com/css2?family=Arimo:wght@400;700&display=swap" rel="stylesheet">
<style>
  :root {
    --backdrop: #4b4b4b;
    --card: #f7f7f5;
    --ink: #1b1b1b;
    --band-black: #1e1e1e;
    --band-red: #b51f24;
    --paper-text: #ffffff;
    --font: "Arimo", Arial, sans-serif;
  }
  * { margin: 0; padding: 0; box-sizing: border-box; }
  html, body { width: 1200px; height: 1000px; overflow: hidden; }
  body { background: var(--backdrop); font-family: var(--font); position: relative; }

  .card {
    position: absolute;
    width: 530px;
    height: 301px;
    background: var(--card);
    border-radius: 16px;
    overflow: hidden;
  }
  .card--front { left: 180px; top: 170px; }
  .card--back  { left: 473px; top: 550px; }

  .brand {
    position: absolute;
    display: flex;
    flex-direction: column;
    align-items: center;
    text-align: center;
    color: var(--ink);
    font-weight: 700;
    text-transform: uppercase;
    line-height: 1.05;
  }
  .brand__dot { border-radius: 50%; background: var(--band-red); }
  .card--front .brand { left: 373px; top: 38px; width: 130px; font-size: 15px; }
  .card--front .brand__dot { width: 40px; height: 40px; margin-bottom: 14px; }
  .card--back .brand { left: 140px; top: 55px; width: 250px; font-size: 28px; }
  .card--back .brand__dot { width: 72px; height: 72px; margin-bottom: 22px; }

  .holder { position: absolute; left: 18px; top: 162px; color: var(--ink); }
  .holder__name { font-size: 16px; font-weight: 700; letter-spacing: 0.3px; text-transform: uppercase; }
  .holder__role { font-size: 12px; margin-top: 3px; }

  .band {
    position: absolute;
    left: 0;
    display: flex;
    align-items: center;
    padding-left: 18px;
    color: var(--paper-text);
    font-size: 12.5px;
    white-space: nowrap;
  }
  .band--address {
    top: 217px; height: 28px; width: 490px;
    background: var(--band-black);
    clip-path: polygon(0 0, 100% 0, 94.5% 100%, 0 100%);
  }
  .band--contact {
    top: 248px; height: 24px; width: 480px;
    background: var(--band-red);
    font-size: 12px;
    clip-path: polygon(0 0, 100% 0, 95% 100%, 0 100%);
  }
  .band b { font-weight: 700; margin-right: 4px; }
  .band .gap { margin-left: 10px; }
</style>
</head>
<body>
  <section class="card card--front">
    <div class="brand">
      <span class="brand__dot"></span>
      <span class="brand__name">Holloway Kenbukan Karate Studio</span>
    </div>
    <div class="holder">
      <p class="holder__name">Sensei Marcus T. Adler</p>
      <p class="holder__role">Instructor</p>
    </div>
    <p class="band band--address">Larkspur Commons, 18342 U.S. Hwy 91, Marlowe, Florida. 33914</p>
    <p class="band band--contact"><b>Phone:</b>407-555-0183<b class="gap">Email:</b>Hollowaykenbukanstudio@mailgrove.example</p>
  </section>

  <section class="card card--back">
    <div class="brand">
      <span class="brand__dot"></span>
      <span class="brand__name">Holloway Kenbukan Karate Studio</span>
    </div>
  </section>
</body>
</html>
```